Obrelo Business Card

Need a double sided business card. Would like the business card to have the logo on one side and the employees details and business contact details on the other.

Business

```html
<!DOCTYPE html>
<html lang="en">
<head>
<meta charset="utf-8">
<title>Obrelo Business Card</title>
<link href="https://fonts.googleapis.com/css2?family=Lato:wght@400;700;900&display=swap" rel="stylesheet">
<style>
  :root {
    --stage: #3a3a3c;
    --paper: #f2f0e9;
    --ink: #2e2e2e;
    --green: #8cc63f;
    --grey: #8b949c;
    --black-card: #1e1e1e;
  }
  html, body {
    margin: 0;
    padding: 0;
    width: 1200px;
    height: 926px;
    overflow: hidden;
    background: var(--stage);
    font-family: "Lato", sans-serif;
  }
  .canvas {
    position: relative;
    width: 1200px;
    height: 926px;
  }
  .card {
    position: absolute;
    left: 290px;
    width: 620px;
    height: 354px;
    border-radius: 3px;
    overflow: hidden;
    box-shadow: 0 10px 30px rgba(0,0,0,0.35);
  }
  .card-back {
    top: 70px;
    background: var(--black-card);
    display: flex;
    align-items: center;
    justify-content: center;
  }
  .card-front {
    top: 490px;
    background: var(--paper);
  }
  .wordmark {
    font-weight: 900;
    color: var(--green);
    letter-spacing: 0.5px;
    line-height: 1;
  }
  .card-back .wordmark { font-size: 64px; }
  .edge-band {
    position: absolute;
    left: 0;
    top: 0;
    width: 96px;
    height: 354px;
    background: linear-gradient(90deg, var(--green) 0%, var(--green) 70%, var(--grey) 100%);
  }
  .identity {
    position: absolute;
    left: 128px;
    top: 70px;
    display: flex;
    align-items: center;
  }
  .identity .wordmark { font-size: 46px; }
  .divider {
    width: 2px;
    height: 58px;
    background: var(--ink);
    margin: 0 18px;
  }
  .person-name {
    font-size: 32px;
    font-weight: 700;
    color: var(--ink);
    margin: 0;
    line-height: 1.05;
  }
  .person-role {
    font-size: 15px;
    color: var(--green);
    margin: 2px 0 0;
  }
  .contact-list {
    position: absolute;
    left: 268px;
    top: 176px;
    margin: 0;
    padding: 0;
    list-style: none;
  }
  .contact-list li {
    display: flex;
    align-items: center;
    font-size: 16px;
    color: var(--ink);
    height: 28px;
  }
  .contact-list svg {
    width: 16px;
    height: 16px;
    margin-right: 12px;
    fill: var(--green);
    flex: none;
  }
</style>
</head>
<body>
<main class="canvas">

  <section class="card card-back" aria-label="Card back">
    <span class="wordmark">Obrelo</span>
  </section>

  <section class="card card-front" aria-label="Card front">
    <div class="edge-band" role="img" aria-label="Decorative green and grey band along the left edge"></div>

    <div class="identity">
      <span class="wordmark">Obrelo</span>
      <span class="divider"></span>
      <div>
        <h1 class="person-name">Daniel Marsh</h1>
        <p class="person-role">Owner/C.E.O</p>
      </div>
    </div>

    <ul class="contact-list">
      <li>
        <svg viewBox="0 0 16 16"><path d="M8 1 L15 8 H13 V15 H9.5 V10.5 H6.5 V15 H3 V8 H1 Z"/></svg>
        27 Fenwick Lane, Leeds, LS2 8QT
      </li>
      <li>
        <svg viewBox="0 0 16 16"><path d="M1 5 Q8 0 15 5 L13 7 L11 5.5 V4.5 H5 V5.5 L3 7 Z M4 7 H12 L14 14 H2 Z"/></svg>
        + 321 - 7654 - 1098
      </li>
      <li>
        <svg viewBox="0 0 16 16"><path d="M4.5 1 H11.5 Q12.5 1 12.5 2 V14 Q12.5 15 11.5 15 H4.5 Q3.5 15 3.5 14 V2 Q3.5 1 4.5 1 Z M5 3 V11.5 H11 V3 Z"/><circle cx="8" cy="13.2" r="0.9" fill="var(--paper)"/></svg>
        + 789 - 3456 - 1012
      </li>
      <li>
        <svg viewBox="0 0 16 16"><path d="M1 3 H15 V4 L8 9 L1 4 Z M1 5.5 L8 10.5 L15 5.5 V13 H1 Z"/></svg>
        hello@obrelo.com
      </li>
      <li>
        <svg viewBox="0 0 16 16"><path d="M6.5 9.5 L9.5 6.5" stroke="var(--green)" stroke-width="1.8" fill="none"/><path d="M7 4.5 L9 2.5 Q10.8 0.7 12.6 2.5 L13.5 3.4 Q15.3 5.2 13.5 7 L11.5 9 L10.4 7.9 L12.4 5.9 Q13.2 5.1 12.4 4.3 L11.7 3.6 Q10.9 2.8 10.1 3.6 L8.1 5.6 Z M9 11.5 L7 13.5 Q5.2 15.3 3.4 13.5 L2.5 12.6 Q0.7 10.8 2.5 9 L4.5 7 L5.6 8.1 L3.6 10.1 Q2.8 10.9 3.6 11.7 L4.3 12.4 Q5.1 13.2 5.9 12.4 L7.9 10.4 Z"/></svg>
        www.obrelo.com
      </li>
    </ul>
  </section>

</main>
</body>
</html>
```